Event Poster Design for Camp for Teenagers

I need graphics designed for our summer camps event. These camps are for teenagers, 6-12th grades. Primary graphic design is for a 11x17 poster but will also need the images resized for social, 16x9 title slide, and a postcard size. Graphic should include the following:Main Title: Pine Ridge Youth Summer CampsDates: High School - June 3-7; Middle School - June 17-21; Ignite - June 24 - 28Register at SDNextGen.comFor each camp, include name and headshot of speaker:High: Ray Whitcomb (guy in blue shirt)Middle: Marla Pettis (girl)Ignite: Joey SilvaInclude Pine Ridge Youth logoBlack Hills Retreat Center, Elk Bend, SDGraphic should be attractive to teenagers. Ideas - geometric shapes, 90's coloring/imagery, bright colors, soft earth tones, etc. Open to ideasMy graphic design experience is VERY limited. I will need help receiving the files I need in the various sizes. Thank you.
Look and feel
Each slider illustrates characteristics of the customer's brand and the style your logo design should communicate.

```html
<!DOCTYPE html>
<html lang="en">
<head>
<meta charset="utf-8">
<title>Pine Ridge Youth Summer Camp</title>
<link rel="stylesheet" href="https://fonts.googleapis.com/css2?family=Baloo+2:wght@700&family=Caveat+Brush&family=Montserrat:wght@800&family=Permanent+Marker&display=swap">
<style>
  :root {
    --bg: #101010;
    --bg-glow: #1d1d1f;
    --brand-blue: #2fb3ec;
    --title-orange: #f2aa33;
    --title-glow: rgba(60, 170, 240, 0.55);
    --ink-light: #f3ecd6;
    --rule: #d9d9d9;
    --ring-yellow: #f5e400;
    --ring-dark: #24343d;
    --photo-tone: #8a7f74;
    --palm-green: #4c6a34;
    --palm-brown: #8a4f1e;
  }
  html, body {
    margin: 0;
    padding: 0;
    overflow: hidden;
    background: var(--bg);
  }
  .poster {
    position: relative;
    width: 776px;
    height: 1200px;
    overflow: hidden;
    background: radial-gradient(ellipse at 50% 85%, var(--bg-glow) 0%, var(--bg) 70%);
  }
  .palm-art {
    position: absolute;
    left: 380px;
    top: 460px;
    width: 390px;
    height: 740px;
    border-radius: 180px 180px 0 0;
    background: linear-gradient(180deg, var(--palm-green) 0%, var(--palm-brown) 100%);
    opacity: 0.18;
  }
  .brand {
    position: absolute;
    top: 120px;
    left: 0;
    width: 100%;
    text-align: center;
    font-family: "Montserrat", sans-serif;
    font-weight: 800;
    font-size: 44px;
    color: var(--brand-blue);
    letter-spacing: 0.5px;
  }
  .title {
    position: absolute;
    top: 250px;
    left: 0;
    width: 100%;
    margin: 0;
    text-align: center;
    font-family: "Permanent Marker", "Caveat Brush", cursive;
    font-weight: 400;
    font-size: 80px;
    line-height: 1;
    color: var(--title-orange);
    letter-spacing: 2px;
    white-space: nowrap;
    text-shadow: 0 0 14px var(--title-glow);
  }
  .rule {
    position: absolute;
    height: 3px;
    background: var(--rule);
  }
  .rule--venue { left: 90px; width: 580px; }
  .rule--venue-top { top: 398px; }
  .rule--venue-bottom { top: 477px; }
  .rule--register { left: 118px; width: 518px; }
  .rule--register-top { top: 1029px; }
  .rule--register-bottom { top: 1099px; }
  .venue, .register {
    position: absolute;
    left: 0;
    width: 100%;
    text-align: center;
    font-family: "Caveat Brush", cursive;
    color: var(--ink-light);
    margin: 0;
    white-space: nowrap;
  }
  .venue { top: 422px; font-size: 32px; }
  .register { top: 1050px; font-size: 32px; }
  .headshot {
    position: absolute;
    border-radius: 50%;
    background: radial-gradient(circle at 50% 40%, #b9a89a 0%, var(--photo-tone) 60%, #4c4a48 100%);
    border: 5px solid var(--ring-yellow);
    box-shadow: 0 0 0 7px var(--ring-dark);
    box-sizing: border-box;
  }
  .headshot--high { left: 30px; top: 546px; width: 236px; height: 236px; }
  .headshot--ignite { left: 482px; top: 548px; width: 232px; height: 232px; }
  .headshot--middle { left: 256px; top: 614px; width: 236px; height: 236px; z-index: 2; }
  .speaker {
    position: absolute;
    width: 300px;
    text-align: center;
    font-family: "Baloo 2", sans-serif;
    font-weight: 700;
    font-size: 19px;
    line-height: 28px;
    color: var(--ink-light);
    text-transform: uppercase;
    letter-spacing: 0.5px;
    margin: 0;
    white-space: nowrap;
  }
  .speaker span { display: block; }
  .speaker .when { margin-top: 4px; }
  .speaker--high { left: 0; top: 800px; }
  .speaker--middle { left: 224px; top: 882px; }
  .speaker--ignite { left: 458px; top: 800px; }
</style>
</head>
<body>
  <main class="poster">
    <div class="palm-art" role="img" aria-label="Painted palm tree silhouette in green and brown"></div>

    <div class="brand">Pine Ridge Youth</div>
    <h1 class="title">SUMMER CAMP</h1>

    <div class="rule rule--venue rule--venue-top"></div>
    <p class="venue">WHERE : Cedar Hollow Retreat Center, Elk Bend</p>
    <div class="rule rule--venue rule--venue-bottom"></div>

    <div class="headshot headshot--high" role="img" aria-label="Headshot of speaker Ray Whitcomb"></div>
    <div class="headshot headshot--ignite" role="img" aria-label="Headshot of speaker Cody Brandt"></div>
    <div class="headshot headshot--middle" role="img" aria-label="Headshot of speaker Marla Pettis"></div>

    <p class="speaker speaker--high">
      <span>Speaker : Ray Whitcomb</span>
      <span>( High School )</span>
      <span class="when">When : June 3-7</span>
    </p>
    <p class="speaker speaker--middle">
      <span>Speaker : Marla Pettis</span>
      <span>( Mid School )</span>
      <span class="when">When : June 17 - 21</span>
    </p>
    <p class="speaker speaker--ignite">
      <span>Speaker : Cody Brandt</span>
      <span>( Ignite )</span>
      <span class="when">When : June 24-28</span>
    </p>

    <div class="rule rule--register rule--register-top"></div>
    <p class="register">REGISTER at PineRidgeYouth.com</p>
    <div class="rule rule--register rule--register-bottom"></div>
  </main>
</body>
</html>
```